Hair Extension Package

I need a high end looking package design for hair extensions. It must include our company logo (either black or white version) and the text that is provided in the attachment. The image of the old package is for dimension purposes only.
Updates
I have added an image of the dimensions the package needs to be.
Thanks
Target Market(s)
Salons and hairdressers would be purchasing this product
Industry/Entity Type
Hair
Look and feel
Each slider illustrates characteristics of the customer's brand and the style your logo design should communicate.

```html
<!DOCTYPE html>
<html lang="en">
<head>
<meta charset="utf-8">
<title>Mane Luxe Extensions – Package Dieline</title>
<link rel="stylesheet" href="https://fonts.googleapis.com/css2?family=Mulish:ital,wght@1,400;1,700&display=swap">
<style>
  :root {
    --canvas: #ffffff;
    --panel-light: #fdf3dc;
    --panel-mid: #f6e2b4;
    --panel-deep: #ecd097;
    --ink: #1c1610;
    --ornament: #b59a6c;
    --art-light: #fbf1d8;
    --art-mid: #e8d9b8;
    --window: #ffffff;
    --swatch-white: #ffffff;
    --swatch-rose: #e98383;
    --swatch-red: #f20d0d;
    --swatch-brown: #3a2a10;
    --swatch-black: #050505;
    --swatch-wine: #6d0a0a;
  }
  * { box-sizing: border-box; margin: 0; padding: 0; }
  html, body { width: 1200px; height: 666px; overflow: hidden; background: var(--canvas); }
  body { font-family: "Mulish", sans-serif; font-style: italic; color: var(--ink); }

  .dieline { position: relative; width: 1200px; height: 666px; }

  .panel {
    position: absolute; top: 50px; height: 490px;
    background: radial-gradient(ellipse at 50% 45%, var(--panel-light) 0%, var(--panel-mid) 65%, var(--panel-deep) 100%);
    overflow: hidden;
  }
  .panel--front { left: 55px; width: 170px; }
  .panel--about { left: 244px; width: 130px; }
  .panel--remy  { left: 384px; width: 130px; }
  .panel--art   { left: 530px; width: 170px; }

  .ornament { position: absolute; z-index: 0; background: var(--ornament); opacity: .28; }
  .ornament--corner-tl { top: 0; left: 0; width: 40px; height: 52px; border-bottom-right-radius: 40px; }
  .ornament--corner-tr { top: 0; right: 0; width: 40px; height: 52px; border-bottom-left-radius: 40px; }
  .ornament--corner-bl { bottom: 0; left: 0; width: 36px; height: 60px; border-top-right-radius: 36px; }
  .ornament--corner-br { bottom: 0; right: 0; width: 36px; height: 60px; border-top-left-radius: 36px; }
  .ornament--bird { top: 136px; left: 4px; width: 26px; height: 30px; border-radius: 50%; }
  .ornament--vine { bottom: 0; right: 0; width: 13px; height: 150px; border-top-left-radius: 13px; }

  .brand-name {
    position: absolute; z-index: 1; top: 88px; left: 10px; right: 6px;
    font-size: 17px; font-weight: 700; color: var(--ink); line-height: 1.05;
  }
  .product-window {
    position: absolute; z-index: 2; left: 15px; top: 180px; width: 141px; height: 310px;
    background: var(--window);
  }

  .copy { position: absolute; z-index: 1; left: 7px; right: 7px; text-align: center; }
  .copy h2 { font-size: 9px; font-weight: 700; margin-bottom: 12px; }
  .copy h3 { font-size: 6px; font-weight: 400; text-transform: uppercase; margin-bottom: 12px; }
  .copy p { font-size: 8.5px; line-height: 1.42; }
  .copy--about { top: 130px; }
  .copy--remy { top: 146px; }

  .contact { position: absolute; z-index: 1; left: 6px; right: 6px; top: 426px; text-align: center; font-size: 8px; font-weight: 700; line-height: 1.3; }
  .tagline { position: absolute; z-index: 1; left: 4px; right: 4px; top: 442px; text-align: center; font-size: 8px; font-weight: 700; line-height: 1.3; }

  .portrait {
    position: absolute; top: 0; left: 0; width: 170px; height: 330px;
    background: linear-gradient(160deg, var(--art-light) 0%, var(--art-mid) 100%);
  }
  .colours { position: absolute; top: 384px; left: 0; right: 0; text-align: center; }
  .colours h4 { font-size: 6px; font-weight: 700; text-transform: uppercase; margin-bottom: 10px; }
  .swatches { display: grid; grid-template-columns: repeat(3, 32px); gap: 13px 8px; justify-content: center; }
  .swatch { width: 32px; height: 32px; border-radius: 50%; }
  .swatch--white { background: var(--swatch-white); }
  .swatch--rose  { background: var(--swatch-rose); }
  .swatch--red   { background: var(--swatch-red); }
  .swatch--brown { background: var(--swatch-brown); }
  .swatch--black { background: var(--swatch-black); }
  .swatch--wine  { background: var(--swatch-wine); }
</style>
</head>
<body>
<main class="dieline">

  <section class="panel panel--front">
    <p class="brand-name">Mane Luxe Extensions</p>
    <div class="ornament ornament--bird" role="img" aria-label="Small perched bird ornament"></div>
    <div class="product-window" aria-label="Clear product window"></div>
    <div class="ornament ornament--vine" role="img" aria-label="Leafy vine ornament"></div>
  </section>

  <section class="panel panel--about">
    <div class="ornament ornament--corner-tl" role="img" aria-label="Floral corner flourish"></div>
    <div class="ornament ornament--corner-tr" role="img" aria-label="Floral corner flourish"></div>
    <div class="copy copy--about">
      <h2>About Our Hair</h2>
      <h3>Premium virgin full cuticle hair</h3>
      <p>Our premium virgin hair extensions are made of only the finest human hair. These 100% human hair extensions will lasts for 1-2 years with proper care. The hair can be styled, curled, straightened or dyed as desired. Bonds are made of an Italian keratin protein which provides a strong and secure hold while letting the hair move naturally. Each bundle contains 25 pieces</p>
    </div>
    <div class="ornament ornament--corner-bl" role="img" aria-label="Floral corner flourish"></div>
    <div class="ornament ornament--corner-br" role="img" aria-label="Floral corner flourish"></div>
    <div class="contact">
      <p>Contact us</p>
      <p>www.maneluxe.ca</p>
      <p>support@maneluxe.ca</p>
      <p>Mane Luxe Extensions Inc.</p>
    </div>
  </section>

  <section class="panel panel--remy">
    <div class="ornament ornament--corner-tl" role="img" aria-label="Floral corner flourish"></div>
    <div class="ornament ornament--corner-tr" role="img" aria-label="Floral corner flourish"></div>
    <div class="copy copy--remy">
      <h2>INDIAN REMY HAIR</h2>
      <p>Our Indian hair extensions are made of only the finest Indian premium remy hair. These 100% human hair extensions will lasts for 5-6 months of wear. The hair can be styled, curled or straightened as desired. Bonds are made of a Italian keratin protein which provides a strong and secure hold while letting the hair move naturally. Each bundle contains 25 pieces</p>
    </div>
    <div class="ornament ornament--corner-bl" role="img" aria-label="Floral corner flourish"></div>
    <div class="ornament ornament--corner-br" role="img" aria-label="Floral corner flourish"></div>
    <div class="tagline">
      <p>Professional Hair Extensions</p>
      <p>Silky soft &amp; tangle free</p>
      <p>Long Lasting, True Remy Hair</p>
    </div>
  </section>

  <section class="panel panel--art">
    <div class="portrait" role="img" aria-label="Line-art illustration of a woman with long flowing hair"></div>
    <div class="colours">
      <h4>Also available in different colors</h4>
      <div class="swatches">
        <span class="swatch swatch--white"></span>
        <span class="swatch swatch--rose"></span>
        <span class="swatch swatch--red"></span>
        <span class="swatch swatch--brown"></span>
        <span class="swatch swatch--black"></span>
        <span class="swatch swatch--wine"></span>
      </div>
    </div>
  </section>

</main>
</body>
</html>
```